Dunmore Plumbing LLC business card

Would like a modern looking business card with my new logo

Contact Information for Business Card

Calvin Dunmore 2418 Elm Hollow Rd Southbury, CT 06999, Dunmoreplumbingllc@exampletrade.com, 203-555-0174

```html
<!DOCTYPE html>
<html lang="en">
<head>
<meta charset="utf-8">
<title>Dunmore Plumbing LLC — Business Card</title>
<link rel="stylesheet" href="https://fonts.googleapis.com/css2?family=Arimo:wght@400;700&display=swap">
<style>
  :root {
    --page: #e6e6e4;
    --card: #ffffff;
    --ink: #2b2b2d;
    --text: #4a4a4c;
    --blue: #0ea4e4;
    --blue-deep: #0a95d2;
    --mist: #e3e3e3;
    --mist-light: #f1f1f1;
    --black-band: #222226;
  }
  * { box-sizing: border-box; margin: 0; padding: 0; }
  html, body { width: 1200px; height: 801px; overflow: hidden; }
  body {
    background: var(--page);
    font-family: "Arimo", Arial, sans-serif;
    position: relative;
  }
  .card {
    position: absolute;
    width: 540px;
    height: 309px;
    top: 246px;
    overflow: hidden;
    box-shadow: 0 6px 18px rgba(0,0,0,0.18);
  }
  /* Front */
  .card-front { left: 40px; background: var(--card); }
  .card-front .column-band {
    position: absolute; left: 330px; top: 0; width: 140px; bottom: 12px;
    background: var(--mist-light);
  }
  .card-front .fixture-art {
    position: absolute; left: 20px; top: 18px; width: 380px; height: 110px;
    background: linear-gradient(90deg, var(--mist-light), var(--mist));
    border-radius: 10px;
  }
  .card-front .base-band {
    position: absolute; left: 0; bottom: 0; height: 12px; width: 72%;
    background: var(--blue);
  }
  .card-front .base-band-dark {
    position: absolute; right: 0; bottom: 0; height: 12px; width: 28%;
    background: var(--black-band);
  }
  .brand-name {
    position: absolute; left: 28px; top: 146px;
    font-weight: 700; font-size: 28px; line-height: 1; letter-spacing: 0.5px;
    color: var(--ink); text-transform: uppercase; white-space: nowrap;
    display: flex; align-items: center; gap: 10px;
  }
  .brand-name .mark {
    width: 16px; height: 16px; background: var(--blue); display: inline-block;
  }
  .holder-name {
    position: absolute; left: 28px; top: 192px;
    font-weight: 700; font-size: 20px; line-height: 1; color: var(--blue);
    text-transform: uppercase; letter-spacing: 0.5px; white-space: nowrap;
  }
  .contact-list {
    position: absolute; left: 28px; top: 228px; list-style: none;
    font-size: 14px; line-height: 1.2; color: var(--text);
  }
  .contact-list li { display: flex; align-items: center; gap: 8px; margin-bottom: 9px; white-space: nowrap; }
  .contact-list svg { width: 14px; height: 14px; flex: none; }
  .address {
    position: absolute; right: 24px; bottom: 28px; text-align: right;
    font-size: 14px; line-height: 1.4; color: var(--text); font-style: normal;
    white-space: nowrap;
  }
  /* Back */
  .card-back {
    left: 620px;
    background: linear-gradient(135deg, var(--blue) 0%, var(--blue-deep) 100%);
  }
  .card-back .pattern-field {
    position: absolute; inset: 0;
    background: linear-gradient(135deg, rgba(255,255,255,0.06), rgba(0,0,0,0.06));
  }
  .card-back .brand-name {
    left: auto; right: 30px; top: auto; bottom: 40px;
    font-size: 22px; color: #ffffff;
  }
</style>
</head>
<body>
  <section class="card card-front" aria-label="Business card front">
    <div class="column-band"></div>
    <div class="fixture-art" role="img" aria-label="Faint grey plumbing fixture illustration"></div>
    <div class="base-band"></div>
    <div class="base-band-dark"></div>
    <div class="brand-name"><span class="mark"></span>Dunmore Plumbing LLC</div>
    <div class="holder-name">Calvin Dunmore</div>
    <ul class="contact-list">
      <li>
        <svg viewBox="0 0 24 24" aria-hidden="true"><path fill="#0ea4e4" d="M6.6 10.8a15 15 0 0 0 6.6 6.6l2.2-2.2a1 1 0 0 1 1-.25 11.4 11.4 0 0 0 3.6.57 1 1 0 0 1 1 1V20a1 1 0 0 1-1 1A17 17 0 0 1 3 4a1 1 0 0 1 1-1h3.5a1 1 0 0 1 1 1c0 1.25.2 2.450.57 3.57a1 1 0 0 1-.25 1z"/></svg>
        203-555-0174
      </li>
      <li>
        <svg viewBox="0 0 24 24" aria-hidden="true"><path fill="#0ea4e4" d="M2 5h20v14H2z"/><path fill="none" stroke="#fff" stroke-width="1.6" d="M2 5l10 8 10-8"/></svg>
        Dunmoreplumbingllc@exampletrade.com
      </li>
    </ul>
    <address class="address">2418 Elm Hollow Rd<br>Southbury, CT 06999</address>
  </section>

  <section class="card card-back" aria-label="Business card back">
    <div class="pattern-field" role="img" aria-label="Repeating embossed brand name pattern on blue"></div>
    <div class="brand-name">Dunmore Plumbing LLC</div>
  </section>
</body>
</html>
```